Home Improvements Website

I would like a website that matches our business colour scheme and uses the fonts consistent without logo. (Monserrat, Chosence & Big Noddle Tiling).
We will need numerous sections: homepage, about us, services (with tiles or links to each service - building, landscaping, decking, maintenance, roofing, gutters etc) current projects (which must be easily editable by me, who is not too tech savvy) and a contacts page with enquiry form we can link to our job management service (Tradify).

```html
<!DOCTYPE html>
<html lang="en">
<head>
<meta charset="utf-8">
<title>Kestrel Home Improvements</title>
<link rel="stylesheet" href="https://fonts.googleapis.com/css2?family=Montserrat:ital,wght@0,400;0,500;0,600;0,700;0,800;1,400&display=swap">
<style>
:root{
  --green:#3aa02c;
  --green-light:#79c043;
  --green-dark:#0e8f36;
  --ink:#222222;
  --text:#2b2b2b;
  --muted:#6c6c6c;
  --pale:#f3fbea;
  --white:#ffffff;
  --footer:#222222;
  --star:#f2b705;
}
*{box-sizing:border-box;margin:0;padding:0}
html,body{width:1200px;height:3976px;overflow:hidden}
body{position:relative;font-family:'Montserrat',sans-serif;color:var(--text);background:var(--white)}
.abs{position:absolute}
.ph{position:absolute}
.btn{position:absolute;background:var(--green);color:var(--white);font-weight:700;font-size:15px;display:flex;align-items:center;justify-content:center;border-radius:3px;letter-spacing:.2px}
.eyebrow{position:absolute;font-size:15px;letter-spacing:7px;color:var(--green);font-weight:500;text-transform:uppercase}
.eyebrow b{font-weight:600;color:var(--green)}
.title{position:absolute;font-weight:700;color:var(--ink);text-transform:uppercase}

/* header */
.topline{left:0;top:0;width:1200px;height:4px;background:var(--green-light)}
.header{left:0;top:0;width:1200px;height:108px;background:var(--white);box-shadow:0 2px 6px rgba(0,0,0,.12);z-index:3}
.brand{left:100px;top:10px;width:140px;height:160px;z-index:5;display:flex;flex-direction:column;align-items:center;justify-content:center;gap:8px}
.brand .mark{width:34px;height:34px;background:var(--green)}
.brand .name{font-weight:800;font-size:20px;color:var(--ink);text-align:center;line-height:1.15}
.contact-item{top:10px;display:flex;align-items:center;gap:8px;z-index:4}
.contact-item .ico{width:34px;height:34px;border-radius:6px;background:var(--green);display:flex;align-items:center;justify-content:center}
.contact-item small{display:block;font-size:8px;color:var(--muted);letter-spacing:.3px}
.contact-item strong{display:block;font-size:16px;font-weight:700;color:var(--ink)}
.nav{left:312px;top:72px;display:flex;gap:42px;font-size:14px;font-weight:500;color:var(--ink);z-index:4}
.nav .on{font-weight:700}
.quote{left:866px;top:58px;width:232px;height:38px;z-index:4;font-size:16px}

/* hero */
.hero{left:0;top:108px;width:1200px;height:712px}
.hero-shape{left:0;top:620px;width:1200px;height:200px}
.hero-panel{left:104px;top:310px;width:440px;height:186px;background:rgba(255,255,255,.08);border-radius:6px}
.hero h1,.hero-h1{left:118px;top:326px;font-size:56px;font-weight:800;color:var(--white);line-height:1}
.hero-sub{left:118px;top:385px;font-size:35px;font-weight:800;color:var(--white)}
.hero-btn{left:117px;top:448px;width:145px;height:37px}
.dots{left:562px;top:752px;display:flex;gap:9px}
.dots i{width:12px;height:12px;border-radius:50%;background:var(--white);display:block}

/* about */
.about-frame{left:108px;top:864px;width:442px;height:420px;border:6px solid var(--green-light)}
.about-img1{left:102px;top:870px;width:440px;height:416px;background:linear-gradient(160deg,#5b6c5a,#2e3429 55%,#4b5a2e)}
.about-img2{left:352px;top:1096px;width:250px;height:228px;background:linear-gradient(150deg,#cfd7db,#d5e04b 55%,#6d7b34);border:5px solid var(--white)}
.about-text{left:655px;top:1050px;width:445px;font-size:12.5px;line-height:20px;color:var(--muted)}
.about-text p{margin-bottom:13px}
.about-btn{left:657px;top:1238px;width:224px;height:40px}

/* services */
.services{left:0;top:1408px;width:1200px;height:582px;background:linear-gradient(180deg,#7ac143 0%,#3aa837 60%,#139a3b 100%)}
.services .eyebrow,.services .title{color:var(--white)}
.svc-arrow{top:1483px;width:38px;height:40px}
.card{top:1546px;width:322px;height:360px;border-radius:10px;overflow:hidden}
.card .label{position:absolute;left:12px;right:14px;bottom:12px;display:flex;justify-content:space-between;align-items:center;color:var(--white);font-weight:700;font-size:17px}
.card-shade{position:absolute;left:0;right:0;bottom:0;height:120px;background:linear-gradient(transparent,rgba(0,0,0,.7))}

/* testimonials */
.quote-card{top:2143px;width:491px;height:245px;background:var(--white);box-shadow:0 2px 10px rgba(0,0,0,.12);padding:24px 22px}
.quote-card p{margin-top:18px;font-size:12.5px;font-style:italic;line-height:23px;color:#444;text-align:justify}
.author{display:flex;align-items:center;gap:10px;margin-top:14px}
.avatar{width:44px;height:44px;border-radius:50%;background:linear-gradient(#9aa3a8,#3a3f44)}
.author strong{display:block;font-size:17px;color:var(--ink)}
.stars{color:var(--star);font-size:13px;letter-spacing:1px;line-height:1}
.t-arrow{top:2254px}

/* projects */
.projects{left:0;top:2460px;width:1200px;height:1100px;background:var(--pale)}
.proj{background:#888}

/* contact */
.footer{left:0;top:3500px;width:1200px;height:476px;background:var(--footer)}
.form-box{left:102px;top:3224px;width:996px;height:423px;border-radius:16px;background:linear-gradient(135deg,#6fbd42 0%,#2aa236 55%,#139137 100%)}
.field{position:absolute;background:var(--white);border:1px solid #ccc;font-size:14px;color:#777;padding:0 13px;display:flex;align-items:center}
.submit{left:528px;top:3567px;width:143px;height:36px;background:var(--ink);color:var(--white);font-weight:700;font-size:15px;display:flex;align-items:center;justify-content:center;border-radius:2px}

/* footer */
.f-brand{left:100px;top:3692px;width:175px;height:176px;display:flex;flex-direction:column;align-items:center;justify-content:center;gap:10px}
.f-brand .mark{width:40px;height:40px;background:var(--green)}
.f-brand .name{font-weight:800;font-size:24px;color:var(--white);text-align:center;line-height:1.15}
.f-head{font-size:16px;font-weight:600;color:var(--white);text-transform:uppercase}
.f-head span{border-bottom:2px solid var(--green)}
.f-list{font-size:13.5px;color:#e6e6e6;line-height:31px;list-style:none}
.f-line{display:flex;gap:8px;font-size:13.5px;color:#e6e6e6;line-height:20px}
.map{left:882px;top:3738px;width:216px;height:142px;background:linear-gradient(135deg,#eceae6,#d9d7d2);border:2px solid #fff}
.copy{left:102px;top:3934px;font-size:13px;color:#e6e6e6}
.social{top:3924px;width:34px;height:34px;border-radius:50%;background:var(--white)}
</style>
</head>
<body>

<!-- header -->
<div class="abs header"></div>
<div class="abs topline" style="z-index:4"></div>
<div class="abs brand" style="background:var(--white);border-radius:0 0 8px 8px">
  <span class="mark"></span>
  <span class="name">KESTREL<br>HOME</span>
</div>

<div class="abs contact-item" style="left:448px">
  <span class="ico"><svg width="18" height="18" viewBox="0 0 24 24" fill="#fff"><path d="M6.6 10.8a15.1 15.1 0 0 0 6.6 6.6l2.2-2.2c.3-.3.7-.4 1-.2 1.1.4 2.3.6 3.6.6.6 0 1 .4 1 1V20c0 .6-.4 1-1 1A17 17 0 0 1 3 4c0-.6.4-1 1-1h3.5c.6 0 1 .4 1 1 0 1.3.2 2.5.6 3.6.1.3 0 .7-.2 1z"/></svg></span>
  <span><small>CALL DANIEL</small><strong>0412 508 274</strong></span>
</div>
<div class="abs contact-item" style="left:610px">
  <span class="ico"><svg width="18" height="18" viewBox="0 0 24 24" fill="#fff"><path d="M6.6 10.8a15.1 15.1 0 0 0 6.6 6.6l2.2-2.2c.3-.3.7-.4 1-.2 1.1.4 2.3.6 3.6.6.6 0 1 .4 1 1V20c0 .6-.4 1-1 1A17 17 0 0 1 3 4c0-.6.4-1 1-1h3.5c.6 0 1 .4 1 1 0 1.3.2 2.5.6 3.6.1.3 0 .7-.2 1z"/></svg></span>
  <span><small>CALL MEGAN</small><strong>0438 772 915</strong></span>
</div>
<div class="abs contact-item" style="left:773px">
  <span class="ico"><svg width="18" height="14" viewBox="0 0 24 18" fill="none" stroke="#fff" stroke-width="2"><rect x="1" y="1" width="22" height="16" rx="2"/><path d="M1 2l11 8 11-8"/></svg></span>
  <span><small>EMAIL US</small><strong style="font-size:14px">info@kestrelhomeimprovements.com</strong></span>
</div>

<nav class="abs nav">
  <span class="on">HOME</span><span>ABOUT US</span><span>SERVICES</span><span>PROJECTS</span><span>CONTACT US</span>
</nav>
<div class="btn quote">REQUEST A FREE QUOTE</div>

<!-- hero -->
<div class="abs hero ph" role="img" aria-label="Landscaper laying turf rolls beside a paved garden path and timber fence" style="background:linear-gradient(180deg,#4b3a2e 0%,#6c5a4a 35%,#9c8c74 55%,#5f8a3a 80%,#3d6b22 100%)"></div>
<svg class="abs hero-shape" viewBox="0 0 1200 200" preserveAspectRatio="none">
  <polygon points="0,0 600,198 1200,0 1200,200 0,200" fill="#ffffff"/>
  <polygon points="0,0 600,180 1200,0 1200,18 600,198 0,18" fill="#222222"/>
</svg>
<div class="abs hero-panel"></div>
<div class="abs hero-h1">WE'RE DOING</div>
<div class="abs hero-sub">WHAT WE DO BEST!</div>
<div class="btn hero-btn">GET STARTED</div>
<div class="abs dots"><i></i><i></i><i></i><i></i></div>

<!-- about -->
<div class="abs about-frame"></div>
<div class="ph about-img1" role="img" aria-label="Two-storey stone house at dusk with lit windows"></div>
<div class="ph about-img2" role="img" aria-label="Two builders in hard hats and hi-vis jackets reviewing plans on a tablet"></div>
<div class="eyebrow" style="left:655px;top:918px">About <b>us</b></div>
<div class="title" style="left:655px;top:944px;font-size:36px;line-height:38px">Welcome to Kestrel<br>Home Improvements</div>
<div class="abs about-text">
  <p>lorem ipsum dolor sit amet consectetur. condimentum nulla sagittis tellus donec bibendum. varius cursus tincidunt conat id amet. vitae auctor habitasse risus urna viverra. imperdiet adipising cum orci vel id non quis semper malesuada.</p>
  <p>lorem ipsum dolor sit amet consectetur. condimentum nulla sagittis tellus donec bibendum. varius cursus tincidunt conat id amet. vitae auctor habitasse risus urna viverra. imperdiet adipising cum orci vel id non quis semper malesuada.</p>
</div>
<div class="btn about-btn">LEARN MORE ABOUT US</div>

<!-- services -->
<section class="abs services"></section>
<div class="eyebrow" style="left:104px;top:1464px;color:#fff">Our services</div>
<div class="title" style="left:104px;top:1488px;font-size:36px;color:#fff">What we do</div>
<svg class="abs svc-arrow" style="left:1017px" viewBox="0 0 38 40"><polygon points="19,1 37,10.5 37,29.5 19,39 1,29.5 1,10.5" fill="none" stroke="#fff" stroke-width="1.5"/><path d="M27 20H11m5-5-5 5 5 5" stroke="#fff" stroke-width="1.5" fill="none"/></svg>
<svg class="abs svc-arrow" style="left:1061px" viewBox="0 0 38 40"><polygon points="19,1 37,10.5 37,29.5 19,39 1,29.5 1,10.5" fill="#5fb83b" stroke="#fff" stroke-width="1.5"/><path d="M11 20h16m-5-5 5 5-5 5" stroke="#fff" stroke-width="1.5" fill="none"/></svg>

<div class="abs card" style="left:102px">
  <div class="ph" role="img" aria-label="Landscaper rolling out fresh turf beside a garden bed" style="inset:0;background:linear-gradient(160deg,#6f8d4c,#4b6a35 50%,#7b8a63)"></div>
  <div class="card-shade"></div>
  <div class="label">LANDSCAPING <span>⟶</span></div>
</div>
<div class="abs card" style="left:438px">
  <div class="ph" role="img" aria-label="Roofer in hi-vis vest laying terracotta roof tiles" style="inset:0;background:linear-gradient(160deg,#bcd6e8,#d9a07a 55%,#b5643f)"></div>
  <div class="card-shade"></div>
  <div class="label">ROOFING <span>⟶</span></div>
</div>
<div class="abs card" style="left:774px">
  <div class="ph" role="img" aria-label="Tradesman fixing composite decking boards" style="inset:0;background:linear-gradient(160deg,#c8c8c8,#6f6a63 55%,#4c4842)"></div>
  <div class="card-shade"></div>
  <div class="label">DECKING <span>⟶</span></div>
</div>
<div class="abs card" style="left:1110px;opacity:.35">
  <div class="ph" role="img" aria-label="Gutter installation on a house roofline" style="inset:0;background:linear-gradient(160deg,#b9c4c8,#4e8f52)"></div>
  <div class="label">GUTTERS</div>
</div>

<!-- testimonials -->
<div class="eyebrow" style="left:0;width:1200px;text-align:center;top:2062px">Testimonials</div>
<div class="title" style="left:0;width:1200px;text-align:center;top:2082px;font-size:35px">What our customer says</div>
<svg class="abs t-arrow" style="left:60px" width="30" height="20" viewBox="0 0 30 20"><path d="M28 10H3m7-7-7 7 7 7" stroke="#222" stroke-width="2" fill="none"/></svg>
<svg class="abs t-arrow" style="left:1112px" width="30" height="20" viewBox="0 0 30 20"><path d="M2 10h25m-7-7 7 7-7 7" stroke="#222" stroke-width="2" fill="none"/></svg>

<div class="abs quote-card" style="left:102px">
  <svg width="34" height="26" viewBox="0 0 34 26" fill="#3aa02c"><path d="M0 26V14C0 6 4 1 12 0v5c-4 1-6 4-6 8h6v13zm19 0V14c0-8 4-13 12-14v5c-4 1-6 4-6 8h6v13z"/></svg>
  <p>Sed ut perspiciatis unde omnis iste natus error stem accusantium doloremque laudantium, totam rem aperiam, eaque ipsa quae ab illo inventore veritatis et quasi architecto beatae vitae dicta sunt explicabo. Nemo enim ipsam voluptatem quia voluptas sit aspernatur aut odit aut fugit</p>
  <div class="author"><span class="avatar" role="img" aria-label="Customer portrait"></span><span><strong>John Smith</strong><span class="stars">★★★★★</span></span></div>
</div>
<div class="abs quote-card" style="left:609px">
  <svg width="34" height="26" viewBox="0 0 34 26" fill="#3aa02c"><path d="M0 26V14C0 6 4 1 12 0v5c-4 1-6 4-6 8h6v13zm19 0V14c0-8 4-13 12-14v5c-4 1-6 4-6 8h6v13z"/></svg>
  <p>Sed ut perspiciatis unde omnis iste natus error stem accusantium doloremque laudantium, totam rem aperiam, eaque ipsa quae ab illo inventore veritatis et quasi architecto beatae vitae dicta sunt explicabo. Nemo enim ipsam voluptatem quia voluptas sit aspernatur aut odit aut fugit</p>
  <div class="author"><span class="avatar" role="img" aria-label="Customer portrait"></span><span><strong>John Smith</strong><span class="stars">★★★★★</span></span></div>
</div>

<!-- projects -->
<section class="abs projects"></section>
<div class="eyebrow" style="left:0;width:1200px;text-align:center;top:2518px">Our <b>works</b></div>
<div class="title" style="left:0;width:1200px;text-align:center;top:2538px;font-size:35px">Some of our projects</div>
<div class="ph proj" role="img" aria-label="Landscaped garden with pergola, outdoor seating and timber boardwalk" style="left:102px;top:2608px;width:322px;height:264px;background:linear-gradient(160deg,#7b8c63,#3f6a2e 60%,#9a9a8a)"></div>
<div class="ph proj" role="img" aria-label="Partially re-sheeted roof showing timber boards and shingles" style="left:102px;top:2888px;width:322px;height:264px;background:linear-gradient(160deg,#4d5a48,#b98a5a 50%,#4b4b4b)"></div>
<div class="ph proj" role="img" aria-label="Renovated grey weatherboard home with white trim and front garden" style="left:439px;top:2608px;width:322px;height:544px;background:linear-gradient(180deg,#e9ecee 0%,#9a9b93 50%,#5c7d3e 85%,#7da743 100%)"></div>
<div class="ph proj" role="img" aria-label="Roofers replacing shingles on a steep roof under blue sky" style="left:775px;top:2608px;width:322px;height:264px;background:linear-gradient(160deg,#3d7fc7,#6b9ed3 40%,#3a3a3a)"></div>
<div class="ph proj" role="img" aria-label="New concrete patio with timber stairs beside a modern home" style="left:775px;top:2888px;width:322px;height:264px;background:linear-gradient(160deg,#a8a8a4,#6f6f6c 55%,#7da34a)"></div>

<!-- contact -->
<footer class="abs footer"></footer>
<svg class="abs" style="left:0;top:3480px" width="1200" height="50" viewBox="0 0 1200 50"><polygon points="0,30 102,10 102,28 0,50" fill="#79c043"/><polygon points="1098,10 1200,30 1200,50 1098,28" fill="#79c043"/></svg>
<div class="abs form-box"></div>
<div class="eyebrow" style="left:0;width:1200px;text-align:center;top:3272px;color:#fff">Contact us</div>
<div class="title" style="left:0;width:1200px;text-align:center;top:3296px;font-size:35px;color:#fff">How can we help?</div>
<div class="field" style="left:228px;top:3357px;width:363px;height:39px">Name*</div>
<div class="field" style="left:609px;top:3357px;width:363px;height:39px">Phone*</div>
<div class="field" style="left:228px;top:3416px;width:363px;height:39px">Email*</div>
<div class="field" style="left:609px;top:3416px;width:363px;height:39px;justify-content:space-between">Job Category: <span style="color:#333;font-size:10px">▼</span></div>
<div class="field" style="left:228px;top:3472px;width:744px;height:84px;align-items:flex-start;padding-top:10px">Message</div>
<div class="abs submit">SUBMIT</div>

<!-- footer -->
<div class="abs f-brand"><span class="mark"></span><span class="name">KESTREL<br>HOME</span></div>

<div class="abs" style="left:355px;top:3704px">
  <div class="f-head"><span>Quick</span> links</div>
  <ul class="f-list" style="margin-top:8px">
    <li>Home</li><li>About Us</li><li>Services</li><li>Projects</li><li>Contact Us</li>
  </ul>
</div>

<div class="abs" style="left:531px;top:3704px;width:330px">
  <div class="f-head"><span>Connect</span> with us</div>
  <div class="f-line" style="margin-top:12px"><svg width="12" height="16" viewBox="0 0 12 16" fill="#fff"><path d="M6 0a6 6 0 0 0-6 6c0 4.5 6 10 6 10s6-5.5 6-10a6 6 0 0 0-6-6zm0 8.5A2.5 2.5 0 1 1 6 3.5a2.5 2.5 0 0 1 0 5z"/></svg><span>1234 Somestreet<br>Anywhere USA 21212</span></div>
  <div class="f-line" style="margin-top:16px"><svg width="14" height="14" viewBox="0 0 24 24" fill="#fff"><path d="M6.6 10.8a15.1 15.1 0 0 0 6.6 6.6l2.2-2.2c.3-.3.7-.4 1-.2 1.1.4 2.3.6 3.6.6.6 0 1 .4 1 1V20c0 .6-.4 1-1 1A17 17 0 0 1 3 4c0-.6.4-1 1-1h3.5c.6 0 1 .4 1 1 0 1.3.2 2.5.6 3.6.1.3 0 .7-.2 1z"/></svg><span>DANIEL: 0412 508 274</span></div>
  <div class="f-line" style="margin-top:11px;padding-left:22px">MEGAN: 0438 772 915</div>
  <div class="f-line" style="margin-top:13px"><svg width="16" height="12" viewBox="0 0 24 18" fill="#fff"><rect x="0" y="0" width="24" height="18" rx="2"/><path d="M1 2l11 8 11-8" stroke="#222" stroke-width="2" fill="none"/></svg><span>info@kestrelhomeimprovements.com</span></div>
</div>

<div class="abs" style="left:881px;top:3704px"><div class="f-head"><span>Loca</span>tion</div></div>
<div class="ph map" role="img" aria-label="Street map showing the business location"></div>

<div class="abs copy">© 2024 Kestrel Home Improvements All Rights Reserved.</div>
<span class="abs social" style="left:929px"></span>
<span class="abs social" style="left:973px"></span>
<span class="abs social" style="left:1017px"></span>
<span class="abs social" style="left:1061px"></span>

</body>
</html>
```